Business Cards and Stationery for Brook Harlow Supply & Advisory sàrl
Simple
Karim Ait Lounes
Associé gérant
CP 7148
CH-1002 Lausanne
Switzerland
kal@brookharlow.ch
www.brookharlow.ch
Business cards to look fresh, in alignment with logo branding.
Colour scheme, images and writting to coordinate with logo.
We may soon need to change our office address and, possibly add phone and fax numbers, so we need to use a font that I can modify.
We want to use the logo designed through Tessavane.

```html
<!DOCTYPE html>
<html lang="en">
<head>
<meta charset="utf-8">
<title>Brook Harlow Supply &amp; Advisory sàrl — Business Card</title>
<link rel="stylesheet" href="https://fonts.googleapis.com/css2?family=Montserrat:wght@400;600;700&display=swap">
<style>
  :root{
    --bg:#e7e8e6;
    --card:#ffffff;
    --green:#3fae3a;
    --green-dark:#2a8f2c;
    --green-light:#7cc855;
    --orange:#f2a516;
    --ink:#5b5b5b;
    --ink-light:#8a8a8a;
  }
  *{box-sizing:border-box;margin:0;padding:0}
  html,body{width:1200px;height:864px;overflow:hidden}
  body{
    background:var(--bg);
    font-family:"Montserrat",Arial,sans-serif;
    display:flex;align-items:center;justify-content:center;gap:40px;
  }
  .card{
    position:relative;width:540px;height:340px;background:var(--card);
    border-radius:18px;overflow:hidden;
    box-shadow:0 10px 30px rgba(0,0,0,.18);
  }
  /* front */
  .card-front .brand{
    position:absolute;left:0;right:0;top:100px;
    display:flex;flex-direction:column;align-items:center;gap:14px;
  }
  .brand-dot{width:70px;height:70px;border-radius:50%;background:var(--green)}
  .brand-name{font-weight:700;font-size:26px;color:var(--green);letter-spacing:.5px}
  .card-front .website{
    position:absolute;left:0;right:0;bottom:36px;text-align:center;
    font-size:11px;letter-spacing:6px;color:var(--ink);text-transform:uppercase;
  }
  /* back */
  .band{position:absolute;left:0;top:0;width:540px;height:340px}
  .identity{position:absolute;left:34px;top:112px}
  .identity .row{display:flex;align-items:center;gap:12px}
  .identity .brand-dot{width:40px;height:40px}
  .identity .brand-name{font-size:21px}
  .identity .tagline{
    margin-top:4px;margin-left:52px;font-size:9px;font-weight:600;
    letter-spacing:1.6px;text-transform:uppercase;color:var(--green-dark);
  }
  .person{position:absolute;left:34px;top:208px;font-variant:small-caps;color:var(--ink)}
  .person .name{font-size:14px;font-weight:600;color:var(--green-dark);letter-spacing:1px}
  .person .role{font-size:11px;color:var(--ink-light);letter-spacing:1px;margin-bottom:14px}
  .person .address{font-size:11px;letter-spacing:1px;line-height:1.5}
  .contacts{
    position:absolute;left:394px;top:42px;list-style:none;
    color:#fff;font-size:10px;letter-spacing:.5px;line-height:2.1;white-space:nowrap;
  }
  .contacts li{display:flex;align-items:center;gap:7px}
  .contacts .icon{width:9px;height:9px;border-radius:50%;background:#fff;flex:none}
</style>
</head>
<body>

<section class="card card-front" aria-label="Business card front">
  <div class="brand">
    <div class="brand-dot"></div>
    <div class="brand-name">Brook Harlow</div>
  </div>
  <p class="website">www.brookharlow.ch</p>
</section>

<section class="card card-back" aria-label="Business card back">
  <svg class="band" viewBox="0 0 540 340" aria-hidden="true">
    <defs>
      <linearGradient id="bandFill" x1="0" y1="0" x2="1" y2="1">
        <stop offset="0" stop-color="#7cc855"/>
        <stop offset="1" stop-color="#2a8f2c"/>
      </linearGradient>
    </defs>
    <path d="M250 0 C360 40 400 160 395 340 L540 340 L540 0 Z" fill="url(#bandFill)"/>
    <path d="M236 0 C346 40 386 160 381 340" fill="none" stroke="#f2a516" stroke-width="4"/>
  </svg>

  <div class="identity">
    <div class="row">
      <div class="brand-dot"></div>
      <div class="brand-name">Brook Harlow</div>
    </div>
    <div class="tagline">Supply &amp; Advisory sàrl</div>
  </div>

  <div class="person">
    <p class="name">Karim Ait Lounes</p>
    <p class="role">Associé gérant</p>
    <p class="address">CP 7148 CH-1002<br>Lausanne Switzerland</p>
  </div>

  <ul class="contacts">
    <li><span class="icon"></span>+41 21 555 01 20</li>
    <li><span class="icon"></span>+41 79 555 48 13</li>
    <li><span class="icon"></span>+41 21 555 01 21</li>
    <li><span class="icon"></span>kal@brookharlow.ch</li>
    <li><span class="icon"></span>www.brookharlow.ch</li>
  </ul>
</section>

</body>
</html>
```